Wix site for a family history research service / genealogist

Design a Wix website for a genealogy/family history research business.

The colour scheme and logo exist and the main imagery has been selected and purchased. The main emotion I'd like the website to convey is "looking up" - like looking up your family tree, looking up a DNA helix, looking up to your parents, grandparents etc. I want the vibe to be one that is enthusiastic about the potential discoveries in your family's history you can make on my website. My service is to the general public, but the main target group are older people 50+ in Australia (I advertise in retirement homes, on golf courses etc.).
I'd like the website to be
- friendly, warm, approachable, trustworthy and open in terms of it's feel
- easy to read, understand and navigate for older people (this is important)
- feature a "language switch" that allows for 3 languages. Ideally pre-selected by geographic origin of visitor.
- Show clear pathways to action (contact or purchase)
- Has a simply shopping cart function that connects to PayPal

The website sections are as follows:
1. A general "Home" page or section
2. About us/me
3. Services (there will be an initial 4 products/services)
3.1 Traditional genealogy (2 products)
3.2 DNA-based ancestry tracing (2 products)
4. Case studies (initially 2)
5. Contact
(The headings are only indicative at this stage)
There is no pre-existing content yet. I'd like to work with lorem ipsum at the beginning. Some more imagery may have to be acquired, I am expecting that.
So far there is only a Facebook page https://www.examplebook.test/profile.php?id=48305716629384

Target Market(s)

Older people in Australia, more males than females

Industry/Entity Type

Personal services - Genealogy

Font styles to use
Serif
Decorative

Colors

Designer to choose colors to be used in the design.

Requirements
Must have
• Feel warm, feel trustworthy, clear call to action
Should not have
• Too small writing, confusing imagery

```html
<!DOCTYPE html>
<html lang="en">
<head>
<meta charset="utf-8">
<title>Henry J. Whitlock – Family History Specialist</title>
<link href="https://fonts.googleapis.com/css2?family=Merriweather:wght@400;700;900&family=Roboto:wght@400;500;700&family=Poppins:wght@500;600&display=swap" rel="stylesheet">
<style>
:root{
  --green:#0f5b2a;
  --green-dark:#0b4a21;
  --beige:#f3ebdf;
  --ink:#1d1d1d;
  --text:#3a3a3a;
  --white:#ffffff;
  --black:#000000;
}
*{box-sizing:border-box;margin:0;padding:0}
html,body{width:1200px;height:4549px;overflow:hidden}
body{position:relative;background:var(--white);font-family:"Roboto",sans-serif;color:var(--text)}
.serif{font-family:"Merriweather",serif}
.abs{position:absolute}
.btn{display:inline-block;background:var(--green);color:var(--white);font-family:"Merriweather",serif;font-weight:700;font-size:15px;padding:13px 26px;text-decoration:none;letter-spacing:.3px}
.section-title{font-family:"Merriweather",serif;font-weight:900;font-size:32px;text-align:center;color:var(--ink)}
.section-title::after{content:"";display:block;width:50px;height:3px;background:var(--green);margin:14px auto 0}
.body-copy{font-size:14.5px;line-height:31px;color:var(--text)}

/* header */
.site-header{position:absolute;left:0;top:0;width:1200px;height:85px;background:var(--beige);z-index:5}
.brand{position:absolute;left:96px;top:-30px;width:160px;height:175px;border-radius:0 0 80px 80px;background:var(--beige);display:flex;flex-direction:column;align-items:center;justify-content:flex-end;padding-bottom:24px;box-shadow:0 6px 0 #b7aea2}
.brand-mark{width:58px;height:58px;border-radius:50%;border:3px solid var(--green);margin-bottom:8px}
.brand-name{font-family:"Merriweather",serif;font-size:13px;color:var(--green);font-weight:400}
.main-nav{position:absolute;left:358px;top:30px;display:flex;gap:48px;font-family:"Merriweather",serif;font-size:15px;color:#222}
.main-nav .active{color:var(--green)}
.cart{position:absolute;left:836px;top:28px;width:18px;height:22px}
.cart-badge{position:absolute;left:852px;top:22px;width:13px;height:13px;border-radius:50%;background:var(--green);color:#fff;font-size:8px;text-align:center;line-height:13px}
.lang{position:absolute;left:880px;top:31px;font-size:14px;color:#222;display:flex;align-items:center;gap:5px}
.nav-cta{position:absolute;left:956px;top:20px;background:var(--green);color:#fff;font-family:"Merriweather",serif;font-weight:700;font-size:15px;padding:13px 15px}

/* hero */
.hero{position:absolute;left:0;top:85px;width:1200px;height:740px}
.hero-photo{position:absolute;inset:0;background:linear-gradient(120deg,#2a3318 0%,#46521f 35%,#5f6b2c 55%,#3a4219 80%,#22290f 100%)}
.hero-copy{position:absolute;left:108px;top:185px;color:#fff}
.hero-copy h1{font-family:"Merriweather",serif;font-weight:900;font-size:48px;line-height:64px}
.hero-copy h2{font-family:"Merriweather",serif;font-weight:700;font-size:21px;margin-top:12px}
.hero-copy p{font-size:15px;line-height:31px;width:460px;margin-top:12px}
.hero-copy .btn{margin-top:14px;font-size:15px;padding:13px 18px}
.arrow{position:absolute;top:285px;width:22px;height:40px}

/* about */
.about{position:absolute;left:0;top:825px;width:1200px;height:613px}
.about-frame{position:absolute;left:108px;top:92px;width:350px;height:330px;border:3px solid var(--green)}
.about-shadow{position:absolute;left:345px;top:298px;width:240px;height:205px;background:var(--beige)}
.about-photo{position:absolute;left:124px;top:106px;width:447px;height:385px;background:linear-gradient(135deg,#8d8a83 0%,#6f6a60 45%,#3f4a63 75%,#263d7a 100%)}
.about-text{position:absolute;left:637px;top:80px;width:440px}
.about-text h2{font-family:"Merriweather",serif;font-weight:900;font-size:30px;color:var(--green)}
.about-text h2::after{content:"";display:block;width:66px;height:3px;background:var(--green);margin:14px 0 20px}
.about-text h3{font-family:"Merriweather",serif;font-weight:700;font-size:20px;color:var(--ink)}
.about-text h4{font-size:16px;font-weight:500;color:var(--ink);margin:10px 0 8px}
.about-text .btn{margin-top:18px}
.faint-seal{position:absolute;left:912px;top:-100px;width:290px;height:290px;border-radius:50%;border:12px solid #e6efe9}

/* services */
.services{position:absolute;left:0;top:1438px;width:1200px;height:844px;background:radial-gradient(ellipse at 50% 40%,#176a33 0%,var(--green-dark) 70%)}
.services .section-title{color:#fff;position:absolute;width:100%;top:80px}
.services .section-title::after{background:#fff}
.service-card{position:absolute;top:314px;width:452px;height:424px;background:var(--beige);text-align:center;padding:180px 30px 0}
.service-img{position:absolute;top:-104px;left:85px;width:282px;height:282px;border-radius:50%;border:5px solid var(--beige)}
.service-name{display:inline-block;border:2px solid var(--green);padding:7px 0;width:378px;font-family:"Merriweather",serif;font-weight:700;font-size:17px;color:var(--green)}
.service-card p{font-size:14px;line-height:30px;margin-top:12px}
.learn{display:inline-block;margin-top:6px;font-family:"Merriweather",serif;font-weight:700;font-size:15px;color:var(--green);text-decoration:underline}

/* case studies */
.cases{position:absolute;left:0;top:2282px;width:1200px;height:1066px}
.cases .section-title{position:absolute;width:100%;top:85px}
.case-text{position:absolute;width:440px}
.case-text h3{font-family:"Merriweather",serif;font-weight:400;font-size:20px;line-height:38px;color:var(--ink);letter-spacing:.2px}
.case-text p{margin:8px 0 20px}
.case-ring{position:absolute;width:376px;height:376px;border-radius:50%;background:var(--beige);box-shadow:0 0 30px rgba(0,0,0,.12)}
.case-photo{position:absolute;left:28px;top:28px;width:320px;height:320px;border-radius:50%;border:4px solid var(--green)}
.case-path{position:absolute;left:400px;top:480px}

/* contact */
.contact{position:absolute;left:0;top:3348px;width:1200px;height:640px;background:var(--beige)}
.contact .section-title{position:absolute;width:100%;top:90px}
.info-item{position:absolute;left:137px;display:flex;gap:28px}
.info-icon{width:82px;height:82px;border-radius:50%;background:var(--green);display:flex;align-items:center;justify-content:center}
.info-item strong{display:block;font-size:15px;color:var(--ink);margin-top:14px;font-weight:700}
.info-item span{display:block;font-size:15px;line-height:26px;margin-top:6px;color:#333}
.field{position:absolute;background:#fff;border:1px solid #ddd;box-shadow:0 2px 6px rgba(0,0,0,.08);font-size:14px;color:#555;padding:16px 16px}
.submit{position:absolute;left:485px;top:444px;width:134px;height:46px;border-radius:23px;background:var(--green);color:#fff;font-family:"Poppins",sans-serif;font-weight:600;font-size:17px;text-align:center;line-height:46px}

/* footer */
.footer-wave{position:absolute;left:0;top:3860px;width:1200px;height:250px}
.site-footer{position:absolute;left:0;top:4060px;width:1200px;height:489px;background:var(--black);color:#fff}
.footer-brand{position:absolute;left:112px;top:88px;width:170px;text-align:center}
.footer-mark{width:146px;height:146px;border-radius:50%;border:4px solid var(--green);margin:0 auto 10px}
.footer-brand .brand-name{font-size:15px;color:var(--green)}
.socials{position:absolute;left:117px;top:290px;display:flex;gap:16px}
.socials a{width:30px;height:30px;border-radius:50%;background:#fff;display:block}
.socials a.fb{background:var(--green)}
.footer-col{position:absolute;top:90px}
.footer-col h4{font-family:"Poppins",sans-serif;font-weight:600;font-size:20px;margin-bottom:10px}
.footer-col li{list-style:none;font-size:15px;line-height:32px;display:flex;align-items:center;gap:12px}
.footer-col li svg{width:13px;height:13px}
.newsletter p{font-size:15px;line-height:30px;width:280px}
.newsletter .email{width:272px;border-bottom:1px solid #fff;font-size:15px;padding:10px 2px 8px}
.newsletter .sub{display:inline-block;margin:30px 0 0 8px;background:#fff;color:var(--green);font-family:"Poppins",sans-serif;font-weight:600;font-size:17px;padding:13px 29px;border-radius:26px}
.footer-rule{position:absolute;left:112px;top:395px;width:976px;height:1px;background:#888}
.copyright{position:absolute;left:0;top:432px;width:100%;text-align:center;font-size:15px}
</style>
</head>
<body>

<header class="site-header">
  <div class="brand">
    <div class="brand-mark"></div>
    <div class="brand-name">WHITLOCK</div>
  </div>
  <nav class="main-nav">
    <span class="active">HOME</span><span>ABOUT US</span><span>SERVICES</span><span>CASE STUDIES</span>
  </nav>
  <svg class="cart" viewBox="0 0 18 22" fill="none" stroke="#333" stroke-width="1.6"><rect x="2" y="7" width="14" height="13" rx="1"/><path d="M6 7V5a3 3 0 0 1 6 0v2"/></svg>
  <div class="cart-badge">0</div>
  <div class="lang">
    <svg width="18" height="18" viewBox="0 0 20 20" fill="none" stroke="#222" stroke-width="1.5"><circle cx="10" cy="10" r="8.5"/><ellipse cx="10" cy="10" rx="3.8" ry="8.5"/><path d="M1.5 10h17M3 5.5h14M3 14.5h14"/></svg>
    EN <svg width="8" height="5" viewBox="0 0 8 5"><path d="M0 0h8L4 5z" fill="#222"/></svg>
  </div>
  <div class="nav-cta">CONTACT US</div>
</header>

<section class="hero">
  <div class="hero-photo" role="img" aria-label="Child sitting high on a huge moss-covered tree in a forest"></div>
  <svg class="arrow" style="left:40px" viewBox="0 0 22 40" fill="none" stroke="#fff" stroke-width="2"><path d="M20 2 2 20l18 18"/></svg>
  <svg class="arrow" style="left:1138px" viewBox="0 0 22 40" fill="none" stroke="#fff" stroke-width="2"><path d="M2 2l18 18L2 38"/></svg>
  <div class="hero-copy">
    <h1>WELCOME TO<br>HENRY J. WHITLOCK</h1>
    <h2>FAMILY HISTORY SPECIALIST</h2>
    <p>Lorem ipsum dolor sit amet, consectetur adipiscing elit, sed do eiusmod tempor incididunt ut labore et dolore aliqua.</p>
    <span class="btn">GET STARTED</span>
  </div>
  <svg class="abs" style="left:0;top:520px" width="1200" height="240" viewBox="0 0 1200 240">
    <path d="M0 200 C150 250 300 240 500 200 C700 160 850 40 1000 50 C1100 55 1160 80 1200 95 V240 H0Z" fill="#fff"/>
    <path d="M235 218 C420 240 560 200 720 130 C850 75 950 40 1030 40 C1110 42 1160 70 1200 90 C1130 55 1060 45 990 55 C870 75 780 140 650 190 C520 235 380 235 235 218Z" fill="var(--green)"/>
  </svg>
</section>

<section class="about">
  <div class="faint-seal"></div>
  <div class="about-frame"></div>
  <div class="about-shadow"></div>
  <div class="about-photo" role="img" aria-label="Portrait of the family history specialist in a jacket against a stone wall"></div>
  <div class="about-text">
    <h2>ABOUT ME</h2>
    <h3>HENRY J. WHITLOCK</h3>
    <h4>FAMILY HISTORY SPECIALIST</h4>
    <p class="body-copy">Lorem ipsum dolor sit amet, consectetur adipiscing elit, sed do eiusmod tempor incididunt ut labore et dolore magna aliqua. Ut enim ad minim veniam, quis nostrud exercitation ullamco laboris nisi ut aliquip ex ea commodo consequat. Duis aute irure dolor in reprehenderit in voluptate velit esse cillum dolore eu fugiat nulla pariatur. Excepteur sint occaecat cupidatat non proident, sunt in culpa qui officia deserunt mollit anim laborum.</p>
    <span class="btn">READ MORE</span>
  </div>
</section>

<section class="services">
  <h2 class="section-title">OUR SERVICES</h2>
  <div class="service-card" style="left:127px">
    <div class="service-img" role="img" aria-label="Woman in a red hat tending plants in a field" style="background:radial-gradient(circle at 50% 40%,#a2573f 0%,#3f6b33 60%,#23421f 100%)"></div>
    <div class="service-name">TRADITIONAL GENEALOGY</div>
    <p>Duis aute irure dolor in reprehenderit in voluptate velit esse cillum dolore eu fugiat nulla pariatur. Excepteur sint occaecat cupidatat non proident, sunt in culpa qui officia deserunt mollit anim id est laborum."</p>
    <span class="learn">Learn More</span>
  </div>
  <div class="service-card" style="left:621px">
    <div class="service-img" role="img" aria-label="Glowing DNA helix growing into a tree" style="background:radial-gradient(circle at 50% 45%,#6f8a5a 0%,#2c4a52 55%,#16262d 100%)"></div>
    <div class="service-name">DNA-BASED ANCESTRY TRACING</div>
    <p>Duis aute irure dolor in reprehenderit in voluptate velit esse cillum dolore eu fugiat nulla pariatur. Excepteur sint occaecat cupidatat non proident, sunt in culpa qui officia deserunt mollit anim id est laborum."</p>
    <span class="learn">Learn More</span>
  </div>
</section>

<section class="cases">
  <h2 class="section-title">CASE STUDIES</h2>
  <div class="case-text" style="left:112px;top:182px">
    <h3>QUIS AUTEM VEL EUM VOLUPTATE REPREHENDERIT VOLUPTATE</h3>
    <p class="body-copy">Lorem ipsum dolor sit amet, consectetur adipiscing elit, sed do eiusmod tempor incididunt ut labore et dolore magna aliqua. Ut enim ad minim veniam, quis nostrud exercitation ullamco laboris nisi ut aliquip ex ea commodo consequat. Duis aute irure dolor in reprehenderit in voluptate velit esse cillum dolore eu fugiat nulla pariatur.</p>
    <span class="btn">READ MORE</span>
  </div>
  <div class="case-ring" style="left:652px;top:168px">
    <div class="case-photo" role="img" aria-label="Older woman with glasses surrounded by flying book pages" style="background:radial-gradient(circle,#7b8a6e 0%,#34503a 60%,#1f3526 100%)"></div>
  </div>
  <svg class="case-path" width="320" height="190" viewBox="0 0 320 190" fill="none">
    <path d="M300 20 C300 90 240 130 185 115 C130 95 60 80 15 160" stroke="var(--green)" stroke-width="2" stroke-dasharray="6 5"/>
    <circle cx="183" cy="114" r="5" fill="var(--green)"/>
  </svg>
  <div class="case-ring" style="left:130px;top:608px">
    <div class="case-photo" role="img" aria-label="Smiling grey-haired woman sitting on a sofa" style="background:radial-gradient(circle,#c9c3bb 0%,#9a9690 55%,#3c4460 100%)"></div>
  </div>
  <div class="case-text" style="left:640px;top:617px">
    <h3>QUIS AUTEM VEL EUM VOLUPTATE REPREHENDERIT VOLUPTATE</h3>
    <p class="body-copy">Lorem ipsum dolor sit amet, consectetur adipiscing elit, sed do eiusmod tempor incididunt ut labore et dolore magna aliqua. Ut enim ad minim veniam, quis nostrud exercitation ullamco laboris nisi ut aliquip ex ea commodo consequat. Duis aute irure dolor in reprehenderit in voluptate velit esse cillum dolore eu fugiat nulla pariatur.</p>
    <span class="btn">READ MORE</span>
  </div>
</section>

<section class="contact">
  <h2 class="section-title">CONTACT US</h2>
  <div class="info-item" style="top:186px">
    <div class="info-icon"><svg width="36" height="26" viewBox="0 0 36 26"><rect width="36" height="26" rx="2" fill="#fff"/><path d="M1 2l17 13L35 2" stroke="var(--green)" stroke-width="3" fill="none"/></svg></div>
    <div><strong>EMAIL:</strong><span>info@whitlockfamily.example</span></div>
  </div>
  <div class="info-item" style="top:290px">
    <div class="info-icon"><svg width="34" height="34" viewBox="0 0 24 24" fill="#fff"><path d="M6.6 10.8a15.1 15.1 0 0 0 6.6 6.6l2.2-2.2a1 1 0 0 1 1-.25 11.4 11.4 0 0 0 3.6.57 1 1 0 0 1 1 1V20a1 1 0 0 1-1 1A17 17 0 0 1 3 4a1 1 0 0 1 1-1h3.5a1 1 0 0 1 1 1c0 1.25.2 2.45.57 3.57a1 1 0 0 1-.25 1z"/></svg></div>
    <div><strong>PHONE:</strong><span>+1 555 0100 2040</span></div>
  </div>
  <div class="info-item" style="top:390px">
    <div class="info-icon"><svg width="28" height="36" viewBox="0 0 28 36" fill="none" stroke="#fff" stroke-width="3"><path d="M14 33s11-12 11-20a11 11 0 0 0-22 0c0 8 11 20 11 20z"/><circle cx="14" cy="13" r="4"/><path d="M4 34h20"/></svg></div>
    <div><strong>ADDRESS:</strong><span>48 Linden Row, Suite 12<br>Maple Bay, CA 90210</span></div>
  </div>
  <div class="field" style="left:485px;top:185px;width:284px;height:50px">First Name</div>
  <div class="field" style="left:779px;top:185px;width:284px;height:50px">Last Name</div>
  <div class="field" style="left:485px;top:247px;width:284px;height:50px">Phone Number</div>
  <div class="field" style="left:779px;top:247px;width:284px;height:50px">Email</div>
  <div class="field" style="left:485px;top:311px;width:578px;height:112px">Message</div>
  <div class="submit">Submit</div>
</section>

<svg class="footer-wave" viewBox="0 0 1200 250" preserveAspectRatio="none">
  <path d="M0 210 C200 180 350 130 560 110 C760 90 980 60 1200 20 V250 H0Z" fill="var(--black)"/>
  <path d="M30 110 C120 160 250 180 400 150 C560 120 760 40 960 40 C800 50 640 120 480 160 C330 200 150 190 30 110Z" fill="var(--green)"/>
</svg>

<footer class="site-footer">
  <div class="footer-brand">
    <div class="footer-mark"></div>
    <div class="brand-name">WHITLOCK</div>
  </div>
  <div class="socials">
    <a class="fb" href="https://www.examplebook.test/profile.php?id=48305716629384" aria-label="Social profile"></a>
    <a aria-label="Social profile"></a>
    <a aria-label="Social profile"></a>
    <a aria-label="Social profile"></a>
  </div>
  <div class="footer-col" style="left:380px">
    <h4>Quick Links</h4>
    <ul>
      <li><svg viewBox="0 0 14 14"><path d="M0 6h9L5 2l1.5-1.5L13 7l-6.5 6.5L5 12l4-4H0z" fill="#fff"/></svg>Home</li>
      <li><svg viewBox="0 0 14 14"><path d="M0 6h9L5 2l1.5-1.5L13 7l-6.5 6.5L5 12l4-4H0z" fill="#fff"/></svg>About Us</li>
      <li><svg viewBox="0 0 14 14"><path d="M0 6h9L5 2l1.5-1.5L13 7l-6.5 6.5L5 12l4-4H0z" fill="#fff"/></svg>Services</li>
      <li><svg viewBox="0 0 14 14"><path d="M0 6h9L5 2l1.5-1.5L13 7l-6.5 6.5L5 12l4-4H0z" fill="#fff"/></svg>Case Studies</li>
      <li><svg viewBox="0 0 14 14"><path d="M0 6h9L5 2l1.5-1.5L13 7l-6.5 6.5L5 12l4-4H0z" fill="#fff"/></svg>Contact Us</li>
    </ul>
  </div>
  <div class="footer-col" style="left:588px">
    <h4>Other Links</h4>
    <ul>
      <li><svg viewBox="0 0 14 14"><path d="M0 6h9L5 2l1.5-1.5L13 7l-6.5 6.5L5 12l4-4H0z" fill="#fff"/></svg>FAQ</li>
      <li><svg viewBox="0 0 14 14"><path d="M0 6h9L5 2l1.5-1.5L13 7l-6.5 6.5L5 12l4-4H0z" fill="#fff"/></svg>Tems of Use</li>
      <li><svg viewBox="0 0 14 14"><path d="M0 6h9L5 2l1.5-1.5L13 7l-6.5 6.5L5 12l4-4H0z" fill="#fff"/></svg>Privacy Policy</li>
      <li><svg viewBox="0 0 14 14"><path d="M0 6h9L5 2l1.5-1.5L13 7l-6.5 6.5L5 12l4-4H0z" fill="#fff"/></svg>Support Links</li>
      <li><svg viewBox="0 0 14 14"><path d="M0 6h9L5 2l1.5-1.5L13 7l-6.5 6.5L5 12l4-4H0z" fill="#fff"/></svg>Conditions</li>
    </ul>
  </div>
  <div class="footer-col newsletter" style="left:802px">
    <h4>Sign Up To Our Newsletter</h4>
    <p>Lorem ipsum dolor sit amet,consectetur adipiscing elit,adipiscing elit.</p>
    <div class="email">Email</div>
    <span class="sub">Subscribe</span>
  </div>
  <div class="footer-rule"></div>
  <div class="copyright">Copyrights@2025.Whitlock Research.All Rights Reserved</div>
</footer>

</body>
</html>
```